Best local air conditioning and heating contractor

We need a website design for a new company in Tampa Bay called the Brightwell Cooling Company. We provide superior services for residential and commercial properties as well as maintenance and installing HVAC systems. We also want to sell equipment, parts and filter on the website as well. We want it easy to use for customers. Rich with content and keywords for our area.

Target Market(s)

homeowners in Tampa Bay

Industry/Entity Type

HVAC air conditioning and heating

Coding

Coded - Design and coding required

Number of Pages Required

5+ page

Font styles to use
Sans Serif

Requirements
Nice to have
• would like the colors to be same as logo

```html
<!DOCTYPE html>
<html lang="en">
<head>
<meta charset="utf-8">
<title>Brightwell Cooling Company – Heating and Air Conditioning Services</title>
<link rel="stylesheet" href="https://fonts.googleapis.com/css2?family=Poppins:wght@400;500;600;700&display=swap">
<style>
:root{
  --red:#e11b22;
  --navy:#0e2a5c;
  --blue:#1d4f91;
  --dark:#0a1433;
  --grey:#efefef;
  --field:#f1f1f1;
  --text:#222;
  --muted:#666;
  --white:#fff;
}
*{box-sizing:border-box;margin:0;padding:0}
html,body{width:1200px;height:4179px;overflow:hidden}
body{position:relative;font-family:"Poppins",sans-serif;color:var(--text);background:var(--white)}
.abs{position:absolute}

/* header */
.topbar{left:543px;top:0;width:657px;height:45px;background:var(--navy);clip-path:polygon(28px 0,100% 0,100% 100%,0 100%);display:flex;align-items:center;color:var(--white);font-size:15px}
.topbar .item{display:flex;align-items:center;gap:12px;margin-left:37px}
.topbar .item:nth-child(2){margin-left:44px}
.topbar .dot{width:22px;height:22px;border-radius:50%;background:var(--red);display:flex;align-items:center;justify-content:center}
.topbar .social{margin-left:auto;margin-right:42px;display:flex;gap:10px}
.topbar .social span{width:14px;height:14px;border-radius:50%;background:var(--white)}
.brand{left:29px;top:24px;width:210px;color:var(--navy);font-weight:700;font-size:21px;line-height:24px;display:flex;gap:10px;align-items:center}
.brand .mark{width:22px;height:22px;background:var(--red);flex:none}
.nav{top:67px;left:0;height:30px;font-size:18px;font-weight:500;color:#222}
.nav a{position:absolute;color:inherit;text-decoration:none;white-space:nowrap}
.btn{background:var(--red);color:var(--white);display:flex;align-items:center;justify-content:center;font-weight:500;text-transform:uppercase}
.quote-top{left:998px;top:57px;width:173px;height:42px;font-size:18px}

/* hero */
.hero-bg{left:0;top:117px;width:1200px;height:1375px;background:var(--grey)}
.hero-svg{left:0;top:0}
.hero-title{left:0;width:1174px;top:250px;text-align:center;font-size:52px;font-weight:600;line-height:66px;color:#2b2b2b}
.hero-text{left:0;width:1174px;top:448px;text-align:center;font-size:20px;line-height:24px;color:#333}
.hero-btn{left:487px;top:579px;width:232px;height:58px;font-size:24px;font-weight:400}

.feature{top:741px;width:224px;height:192px;background:var(--white);border-radius:8px;box-shadow:0 3px 12px rgba(0,0,0,.12);text-align:center}
.feature svg{margin-top:20px}
.feature h3{font-size:16px;font-weight:500;margin-top:6px}
.feature p{font-size:8px;line-height:14px;color:var(--muted);margin:8px 20px 0;text-transform:uppercase}
.feature .more{font-size:11px;color:var(--red);font-weight:600;margin-top:14px}

/* about */
.about-photo{left:101px;top:1057px;width:378px;height:301px;border-radius:6px;background:linear-gradient(120deg,#6b1a1a 0%,#4a2c24 30%,#a48a76 60%,#d8d2c8 100%)}
.badge{left:393px;top:1233px;width:162px;height:162px;border-radius:50%;background:var(--navy);color:var(--white);text-align:center;padding-top:36px}
.badge b{display:block;font-size:56px;font-weight:600;line-height:60px}
.badge span{font-size:12px;font-weight:500}
.about-title{left:587px;top:1088px;font-size:27px;font-weight:600;color:#222}
.about-text{left:592px;top:1140px;width:420px;font-size:14.5px;line-height:17px;color:#666}
.about-text p+p{margin-top:7px}
.about-btn{left:592px;top:1319px;width:167px;height:40px;font-size:15px;text-transform:none;font-weight:400}

/* services */
.section-title{font-size:26px;font-weight:600;color:#222;text-transform:uppercase}
.svc{width:267px;height:251px;border-radius:6px;overflow:hidden}
.svc .img{position:absolute;inset:0}
.svc h3{position:absolute;left:21px;bottom:36px;color:var(--white);font-size:31px;font-weight:400;line-height:38px}
.svc .line{position:absolute;left:21px;bottom:36px;width:145px;height:3px;background:var(--blue)}
.svc.active{background:var(--blue);border:4px solid var(--white);outline:2px solid var(--blue)}
.svc.active h3{position:static;margin:14px 0 0 26px}
.svc.active .line{position:static;margin:2px 0 0 26px}
.svc.active p{color:var(--white);font-size:14px;line-height:24px;margin:18px 24px 0 26px}
.svc.active .tiny{margin:12px 0 0 26px;width:100px;height:18px;font-size:8px}

/* testimonials */
.testi-bg{left:0;top:2378px;width:1200px;height:530px;background:linear-gradient(160deg,#244f8a 0%,#1d4c8c 45%,#20508d 100%)}
.testi-title{left:92px;top:2472px;color:var(--white);font-size:26px;font-weight:600}
.review{top:2592px;width:228px;height:161px;background:var(--white);padding:14px 20px}
.review .stars{color:var(--red);font-size:21px;letter-spacing:2px;line-height:22px}
.review p{font-size:9px;line-height:15px;color:#555;margin-top:8px}
.review .who{display:flex;align-items:center;gap:6px;margin-top:10px}
.review .avatar{width:36px;height:36px;border-radius:50%;background:linear-gradient(#9fc6e3,#2b5d7e)}
.review .name{font-size:10px;font-weight:600;line-height:14px}
.review .role{font-size:7px;color:var(--red);font-weight:600}

.form{left:681px;top:2475px;width:471px;height:493px;background:var(--white);border-radius:8px;box-shadow:0 2px 10px rgba(0,0,0,.12)}
.field{position:absolute;background:var(--field);border-radius:4px;font-size:13px;color:#555;padding:0 17px;display:flex;align-items:center}
.form .send{position:absolute;left:86px;top:428px;width:305px;height:39px;font-size:12px}

/* products */
.product{top:3135px;width:225px;height:271px;background:#f5f5f5;border-radius:14px;box-shadow:0 6px 14px rgba(0,0,0,.06);text-align:center}
.product .pimg{width:120px;height:112px;margin:26px auto 0;border-radius:3px}
.product h4{font-size:15px;font-weight:500;margin-top:14px}
.product .price{font-size:22px;font-weight:600;color:var(--red);margin-top:4px}
.product .price s{color:#777;font-weight:500}
.product .buy{width:120px;height:32px;margin:14px auto 0;font-size:9px}

/* footer */
.footer-svg{left:0;top:3500px}
.footer-brand{left:487px;top:3596px;width:275px;height:110px;background:var(--white);color:var(--navy);font-weight:700;font-size:21px;line-height:25px;display:flex;align-items:center;justify-content:center;gap:10px;text-align:left}
.footer-brand .mark{width:20px;height:20px;background:var(--red);flex:none}
.fcol{top:3785px;color:var(--white)}
.fcol h4{font-size:17px;font-weight:600}
.fcol .bar{width:50px;height:3px;background:var(--blue);margin-top:12px}
.fcol p.body{font-size:13.5px;line-height:27px;margin-top:34px;width:245px}
.fsocial{display:flex;gap:11px;margin-top:24px}
.fsocial span{width:39px;height:39px;border-radius:50%;background:var(--blue)}
.crow{display:flex;gap:18px;margin-top:0}
.crow svg{flex:none;margin-top:4px}
.crow b{display:block;font-size:14px;font-weight:600}
.crow span{font-size:14px;line-height:22px}
.links a{display:flex;justify-content:space-between;color:var(--white);text-decoration:none;font-size:13px;height:40px;align-items:center;border-bottom:1px solid rgba(255,255,255,.12);width:255px}
</style>
</head>
<body>

<!-- top bar -->
<div class="abs topbar">
  <div class="item"><span class="dot"><svg width="12" height="9" viewBox="0 0 12 9"><rect x=".5" y=".5" width="11" height="8" fill="none" stroke="#fff"/><path d="M.5.5 6 5l5.5-4.5" fill="none" stroke="#fff"/></svg></span>info@brightwellcooling.com</div>
  <div class="item"><span class="dot"><svg width="12" height="12" viewBox="0 0 24 24"><path d="M6.6 10.8a15 15 0 0 0 6.6 6.6l2.2-2.2c.3-.3.7-.4 1-.2 1.1.4 2.3.6 3.6.6.6 0 1 .4 1 1V20c0 .6-.4 1-1 1A17 17 0 0 1 3 4c0-.6.4-1 1-1h3.5c.6 0 1 .4 1 1 0 1.3.2 2.5.6 3.6.1.3 0 .7-.2 1z" fill="#fff"/></svg></span>(813) 555-0142</div>
  <div class="social"><span></span><span></span><span></span></div>
</div>

<div class="abs brand"><span class="mark"></span>BRIGHTWELL COOLING COMPANY</div>

<nav class="abs nav">
  <a style="left:320px">HOME</a>
  <a style="left:420px">ABOUT</a>
  <a style="left:530px">SERVICES</a>
  <a style="left:664px">PRODUCTS</a>
  <a style="left:819px">FINANCING</a>
</nav>
<div class="abs btn quote-top">Get a Quote</div>

<!-- hero -->
<div class="abs hero-bg"></div>
<svg class="abs hero-svg" width="1200" height="1000" viewBox="0 0 1200 1000">
  <defs>
    <linearGradient id="heroPhoto" x1="0" y1="0" x2="1" y2="1">
      <stop offset="0" stop-color="#cfc9c1"/>
      <stop offset=".5" stop-color="#e2ddd6"/>
      <stop offset="1" stop-color="#c9c4bd"/>
    </linearGradient>
  </defs>
  <path role="img" aria-label="Technician servicing a ceiling air conditioning unit" d="M0 117H1200V608C900 1000 200 920 0 673Z" fill="url(#heroPhoto)"/>
  <path d="M0 673C200 920 900 1000 1200 608" fill="none" stroke="#e11b22" stroke-width="13"/>
</svg>

<h1 class="abs hero-title">HEATING AND<br>AIR CONDITIONING<br>SERVICES</h1>
<p class="abs hero-text">Lorem ipsum dolor sit amet, consectetuer adipiscing elit.<br>Aenean commodo ligula eget dolor.<br>Aenean massa. Cum sociis natoque penatibus et<br>magnis dis parturient montes, nascetur ridiculus mus.</p>
<div class="abs btn hero-btn">Get a Quote</div>

<div class="abs feature" style="left:214px">
  <svg width="60" height="54" viewBox="0 0 60 54" fill="none" stroke="#1d4f91" stroke-width="2"><rect x="4" y="22" width="40" height="22" rx="2"/><path d="M10 22v22M18 22v22M26 22v22M34 22v22"/><path d="M44 30h8V8a5 5 0 0 0-10 0v6"/><circle cx="47" cy="10" r="6"/></svg>
  <h3>Heating</h3>
  <p>Lorem ipsum dolor sit amet,<br>consectetuer adipiscing elit.</p>
  <div class="more">READ MORE</div>
</div>
<div class="abs feature" style="left:511px">
  <svg width="60" height="54" viewBox="0 0 60 54" fill="none" stroke="#1d4f91" stroke-width="2"><rect x="4" y="4" width="52" height="16" rx="2"/><path d="M10 14h40"/><circle cx="24" cy="36" r="12"/><circle cx="24" cy="36" r="3"/><path d="M24 24v9M24 39v9M12 36h9M27 36h9"/></svg>
  <h3>Cooling</h3>
  <p>Lorem ipsum dolor sit amet,<br>consectetuer adipiscing elit.</p>
  <div class="more">READ MORE</div>
</div>
<div class="abs feature" style="left:809px">
  <svg width="60" height="58" viewBox="0 0 60 58" fill="none" stroke="#1d4f91" stroke-width="2.4"><path d="M10 50 38 22"/><path d="M36 14a9 9 0 0 0 12 12l-6-2-4-4z"/><path d="M50 50 22 22"/><path d="M8 10l6-6 8 8-6 6z"/><rect x="44" y="44" width="10" height="10" transform="rotate(45 49 49)"/></svg>
  <h3>Repairs</h3>
  <p>Lorem ipsum dolor sit amet,<br>consectetuer adipiscing elit.</p>
  <div class="more">READ MORE</div>
</div>

<!-- about -->
<div class="abs about-photo" role="img" aria-label="Technician in a blue cap adjusting heating pipes"></div>
<div class="abs badge"><b>10+</b><span>Years of Experience</span></div>
<h2 class="abs about-title">ABOUT US</h2>
<div class="abs about-text">
  <p>Lorem ipsum dolor sit amet, consectetuer adipiscing elit.<br>Aenean commodo ligula eget dolor.<br>Aenean massa. Cum sociis natoque penatibus et<br>magnis dis parturient montes, nascetur ridiculus mus.</p>
  <p>Lorem ipsum dolor sit amet, consectetuer adipiscing elit.<br>Aenean commodo ligula eget dolor.<br>Aenean massa. Cum sociis natoque penatibus et<br>magnis dis parturient montes, nascetur ridiculus mus.</p>
</div>
<div class="abs btn about-btn">Read More</div>

<!-- services -->
<h2 class="abs section-title" style="left:418px;top:1574px">What Services We Offer</h2>

<div class="abs svc" style="left:123px;top:1676px">
  <div class="img" role="img" aria-label="Technician fitting gas pipes" style="background:linear-gradient(135deg,#7a5a45,#3c4a6a 55%,#2a3550)"></div>
  <h3>Gas<br>Fitting</h3><span class="line"></span>
</div>
<div class="abs svc active" style="left:457px;top:1676px">
  <h3 style="color:#fff;font-size:31px;font-weight:400;line-height:38px">Pipe<br>Fitting</h3><div class="line"></div>
  <p>Nulla commodo dolor massa, vel pellentesque nulla congue quis.</p>
  <div class="btn tiny">Read More</div>
</div>
<div class="abs svc" style="left:814px;top:1676px">
  <div class="img" role="img" aria-label="Technician installing an outdoor condenser unit" style="background:linear-gradient(135deg,#4c4c4c,#8a8a8a 55%,#3b3b3b)"></div>
  <h3>New<br>Installs</h3><span class="line"></span>
</div>
<div class="abs svc" style="left:123px;top:1998px">
  <div class="img" role="img" aria-label="Technician in a cap working on a wall unit" style="background:linear-gradient(135deg,#6c6a62,#a49d93 55%,#d8d3cc)"></div>
  <h3>Commercial<br>Services</h3><span class="line"></span>
</div>
<div class="abs svc" style="left:457px;top:1998px">
  <div class="img" role="img" aria-label="Workers in hard hats on a building site" style="background:linear-gradient(135deg,#8c8a86,#b26a3a 45%,#4d5a6a)"></div>
  <h3>Building<br>Automations</h3><span class="line"></span>
</div>
<div class="abs svc" style="left:814px;top:1998px">
  <div class="img" role="img" aria-label="Rooftop air conditioning units on a home" style="background:linear-gradient(180deg,#8e8e8e,#6a6a6a 60%,#4f4f4f)"></div>
  <h3>Residential<br>Services</h3><span class="line"></span>
</div>

<!-- testimonials and quote form -->
<div class="abs testi-bg" role="img" aria-label="Blue tinted photo of a technician at work"></div>
<h2 class="abs testi-title">WHAT CLIENT SAYS</h2>
<div class="abs review" style="left:89px">
  <div class="stars">★★★★★</div>
  <p>Interdum et malesuada fames ac ante ipsum primis in faucibus donec tempor nisi neque.</p>
  <div class="who"><span class="avatar" role="img" aria-label="Client portrait"></span><div><div class="name">Dana Whitlock</div><div class="role">MANAGER</div></div></div>
</div>
<div class="abs review" style="left:370px">
  <div class="stars">★★★★★</div>
  <p>Interdum et malesuada fames ac ante ipsum primis in faucibus donec tempor nisi neque.</p>
  <div class="who"><span class="avatar" role="img" aria-label="Client portrait"></span><div><div class="name">Dana Whitlock</div><div class="role">MANAGER</div></div></div>
</div>

<form class="abs form">
  <div class="field" style="left:36px;top:41px;width:394px;height:40px">Name</div>
  <div class="field" style="left:36px;top:99px;width:394px;height:41px">Email</div>
  <div class="field" style="left:36px;top:157px;width:394px;height:39px">Phone</div>
  <div class="field" style="left:36px;top:216px;width:394px;height:40px">Select Service</div>
  <div class="field" style="left:41px;top:273px;width:394px;height:131px;align-items:flex-start;padding-top:16px">Message</div>
  <div class="btn send">Request a Quote Now</div>
</form>

<!-- products -->
<h2 class="abs section-title" style="left:373px;top:3014px">Our Best Sellng Products</h2>
<div class="abs product" style="left:41px">
  <div class="pimg" role="img" aria-label="Blower motor product photo" style="background:radial-gradient(circle,#b8b2a8,#6d675f)"></div>
  <h4>Product Title</h4><div class="price">$100 <s>$150</s></div><div class="btn buy">Buy Now</div>
</div>
<div class="abs product" style="left:329px">
  <div class="pimg" role="img" aria-label="Capacitor with wiring product photo" style="background:radial-gradient(circle,#3a3a3a,#e8e4df 70%)"></div>
  <h4>Product Title</h4><div class="price">$100 <s>$150</s></div><div class="btn buy">Buy Now</div>
</div>
<div class="abs product" style="left:616px">
  <div class="pimg" role="img" aria-label="Coiled sensor cable product photo" style="background:radial-gradient(circle,#ffffff 30%,#9a9a9a 45%,#ffffff 60%)"></div>
  <h4>Product Title</h4><div class="price">$100 <s>$150</s></div><div class="btn buy">Buy Now</div>
</div>
<div class="abs product" style="left:925px">
  <div class="pimg" role="img" aria-label="Coiled sensor cable product photo" style="background:radial-gradient(circle,#ffffff 30%,#9a9a9a 45%,#ffffff 60%)"></div>
  <h4>Product Title</h4><div class="price">$100 <s>$150</s></div><div class="btn buy">Buy Now</div>
</div>

<!-- footer -->
<svg class="abs footer-svg" width="1200" height="679" viewBox="0 0 1200 679">
  <path d="M0 250C150 80 400 20 620 20S1060 90 1200 240V679H0Z" fill="#1d4f91"/>
  <path d="M8 270C160 110 400 46 620 46S1060 110 1200 260V679H8Z" fill="#0a1433"/>
</svg>
<div class="abs footer-brand"><span class="mark"></span><span>BRIGHTWELL<br>COOLING COMPANY</span></div>

<div class="abs fcol" style="left:75px">
  <h4>ABOUT US</h4><div class="bar"></div>
  <p class="body">We are an award winning plumbing company with over 20 years experience in the business. We provide a wide range of services for both residential and commercial clients.</p>
  <div class="fsocial"><span></span><span></span><span></span></div>
</div>

<div class="abs fcol" style="left:370px">
  <h4>CONTACT US</h4><div class="bar"></div>
  <div class="crow" style="margin-top:36px"><svg width="18" height="22" viewBox="0 0 18 22" fill="none" stroke="#8a93a8" stroke-width="1.5"><path d="M9 21s7-7 7-12A7 7 0 0 0 2 9c0 5 7 12 7 12z"/><circle cx="9" cy="9" r="2.5"/></svg><div><b>Address:</b><span>2140 Bayshore Blvd, Tampa, FL</span></div></div>
  <div class="crow" style="margin-top:22px"><svg width="22" height="18" viewBox="0 0 22 18" fill="none" stroke="#8a93a8" stroke-width="1.5"><path d="M2 6c0-3 18-3 18 0v2h-5V6H7v2H2z"/><rect x="4" y="9" width="14" height="8" rx="2"/></svg><div><b>Phone:</b><span>+1 813 555 0176</span></div></div>
  <div class="crow" style="margin-top:22px"><svg width="18" height="24" viewBox="0 0 18 24" fill="none" stroke="#8a93a8" stroke-width="1.5"><rect x="3" y="1" width="12" height="22" rx="2"/><path d="M7 19h4"/></svg><div><b>Mobile:</b><span>+1 813 555 0198</span></div></div>
  <div class="crow" style="margin-top:22px"><svg width="22" height="16" viewBox="0 0 22 16" fill="none" stroke="#8a93a8" stroke-width="1.5"><rect x="1" y="1" width="20" height="14"/><path d="M1 1l10 8 10-8"/></svg><div><b>Email:</b><span>support@brightwellcooling.com</span></div></div>
</div>

<div class="abs fcol links" style="left:663px">
  <h4>QUICK LINKS</h4><div class="bar"></div>
  <div style="margin-top:28px">
    <a>About<span>›</span></a><a>Contact<span>›</span></a><a>News List<span>›</span></a><a>Services<span>›</span></a><a style="border:0">Shop<span>›</span></a>
  </div>
</div>

<div class="abs fcol" style="left:959px">
  <h4>OPENING HOURS</h4><div class="bar"></div>
  <div class="crow" style="margin-top:36px"><svg width="24" height="24" viewBox="0 0 24 24" fill="none" stroke="#8a93a8" stroke-width="1.5"><circle cx="12" cy="12" r="11"/><path d="M12 6v6h5"/></svg><div><b>Monday - Friday</b><span>8:00 AM - 5:00 PM</span></div></div>
  <div class="crow" style="margin-top:22px"><svg width="24" height="24" viewBox="0 0 24 24" fill="none" stroke="#8a93a8" stroke-width="1.5"><circle cx="12" cy="12" r="11"/><path d="M12 6v6h5"/></svg><div><b>Saturday</b><span>9:00 AM - 4:00 PM</span></div></div>
  <div class="crow" style="margin-top:22px"><svg width="24" height="24" viewBox="0 0 24 24" fill="none" stroke="#8a93a8" stroke-width="1.5"><circle cx="12" cy="12" r="11"/><path d="M12 6v6h5"/></svg><div><b>Sunday</b><span>CLOSED</span></div></div>
</div>

</body>
</html>
```